Tri-Fold Flyer for Life Coaching Business

We require a tri-fold DL flyer for our Life Coaching business, Tall Harbor.
The flyer needs to be bold, engaging and professional with broad appeal. Ideally it will include a few images and/or graphics, but shouldn’t be too busy.
As a generalist life coaching business, image selection needs to be broad enough to attract clients who are interested in Career, Relationship or General Life Coaching (think Health, Wealth & Balance). Please feel free to use any images/graphics you think are suitable. We have also purchased a selection of images from PixVault that you may wish to use - these can be viewed on our website www.tallharbor-example.com - originals can be requested.
Unlike a lot of coaching businesses, we are not interested in being too cheesy, flowery or spiritual. Our style is direct, up-front and to the point - we don’t take ourselves too seriously. The flyer should reflect this.
Attached is a basic template that shows the required text and an example of layout - however we are very flexible with the layout/design, so please don’t be limited by this (eg. Image on the front is only used as a placeholder, testimonials may work better somewhere else etc).
Also attached is a copy of our business card and logo. This will give you an idea of the designs that we are already using. Again, this is as a guide only - however we would definitely like to use similar fonts to the business card (Helvetica or Helvetica Neue I think) and have the blue from the logo incorporated. It would be great to see icons (similar to what has been used on the business card) for phone number, email address etc. Different versions of the logo (format, colour etc) are available.
Aside from this we would like you to use your creative flair and show us different versions of the flyer. Thank You and Good Luck!
Updates
Hi everyone,
Industry/Entity Type
Life Coaching
Requirements
Must have
- Brochure should be tri-fold DL
Logo should be included - preferably on back cover
Contact details and call to action should be prominent/obvious

```html
<!DOCTYPE html>
<html lang="en">
<head>
<meta charset="utf-8">
<title>Tall Harbor – Tri-Fold Flyer</title>
<link href="https://fonts.googleapis.com/css2?family=Source+Sans+3:wght@400;600;700&family=Roboto+Condensed:wght@700&family=Arimo:wght@400;700&family=Tinos:ital,wght@1,400;1,700&display=swap" rel="stylesheet">
<style>
  :root {
    --page-bg: #e9e9e9;
    --slate-dark: #3f4042;
    --slate-mid: #6a6b6d;
    --slate-light: #8a8b8d;
    --brand-blue: #1a8fd8;
    --brand-blue-light: #3fb2ef;
    --deep-blue: #0f5f9e;
    --navy: #0b4a86;
    --ink: #1d1d1d;
    --text-grey: #333;
    --white: #fff;
    --bar-grey: #6b6b6b;
  }
  * { margin: 0; padding: 0; box-sizing: border-box; }
  html, body { width: 1200px; height: 868px; overflow: hidden; background: var(--page-bg); }
  .flyer {
    position: absolute; left: 21px; top: 20px;
    width: 1158px; height: 828px;
    display: flex;
    box-shadow: 0 4px 14px rgba(0,0,0,.35);
  }
  .panel { position: relative; width: 386px; height: 828px; overflow: hidden; }

  /* Inside flap */
  .panel--flap { background: radial-gradient(ellipse at 50% 30%, var(--slate-light), var(--slate-mid) 45%, var(--slate-dark) 100%); }
  .question {
    position: absolute; left: 98px; width: 270px;
    font-family: "Source Sans 3", sans-serif; font-weight: 700;
    font-size: 27px; line-height: 31px; color: var(--white);
  }
  .question-dot {
    position: absolute; left: 32px; width: 48px; height: 48px; border-radius: 50%;
    background: radial-gradient(circle at 35% 35%, var(--brand-blue-light), var(--brand-blue));
  }
  .divider {
    position: absolute; left: 60px; width: 270px; height: 2px;
    background: linear-gradient(90deg, transparent, rgba(40,40,40,.8), transparent);
  }
  .flap-photo {
    position: absolute; left: 0; top: 610px; width: 386px; height: 218px;
    background: linear-gradient(180deg, #5a8fc8 0%, #9cc0e2 55%, #e4eef7 100%);
  }
  .wave { position: absolute; left: 0; width: 386px; }

  /* Back */
  .panel--back { background: linear-gradient(90deg, #ffffff 60%, #e2e2e2 100%); }
  .section-bar {
    position: absolute; left: 0; width: 346px; height: 34px;
    border-radius: 0 17px 17px 0;
    background: linear-gradient(90deg, #bdbdbd, var(--bar-grey) 30%, var(--bar-grey) 85%, #9a9a9a);
    font-family: "Arimo", sans-serif; font-weight: 700; font-size: 22px; color: var(--white);
    padding-left: 24px; line-height: 34px;
  }
  .about-text {
    position: absolute; left: 23px; width: 328px;
    font-family: "Arimo", sans-serif; font-size: 11.6px; line-height: 14px;
    color: var(--ink); text-align: justify;
  }
  .testimonials {
    position: absolute; left: 16px; top: 232px; width: 328px; height: 328px; border-radius: 50%;
    background: radial-gradient(circle at 45% 40%, #1e9be2, var(--brand-blue) 70%, #1482c9);
    color: var(--white); text-align: center;
  }
  .testimonials h2 {
    font-family: "Tinos", serif; font-style: normal; font-weight: 400;
    font-size: 22px; letter-spacing: .5px; margin-top: 44px;
  }
  .quote {
    font-family: "Source Sans 3", sans-serif; font-style: italic; font-size: 12.4px; line-height: 17.5px;
    width: 270px; margin: 12px auto 0;
  }
  .quote + .quote { margin-top: 10px; }
  .quote-name { display: block; font-family: "Arimo", sans-serif; font-style: normal; font-weight: 700; font-size: 12.5px; margin-top: 3px; }
  .call-to-action {
    position: absolute; left: 22px; top: 592px; width: 340px;
    font-family: "Tinos", serif; font-style: italic; font-size: 17.5px; line-height: 24px; color: #2e6fb3;
  }
  .call-to-action strong { font-size: 23px; font-weight: 700; }
  .contact-list { position: absolute; left: 24px; top: 706px; list-style: none; }
  .contact-list li {
    display: flex; align-items: center; gap: 9px; height: 26px;
    font-family: "Arimo", sans-serif; font-weight: 700; font-size: 13px; color: var(--text-grey);
  }
  .contact-list li.phone { font-size: 16px; height: 30px; }
  .contact-list svg { width: 14px; height: 14px; }
  .abn { position: absolute; right: 32px; top: 790px; font-family: "Arimo", sans-serif; font-size: 11px; color: var(--ink); }

  /* Front */
  .panel--front { background: linear-gradient(180deg, #ffffff 0%, #f4f8fc 34%, #d7e9f8 40%, #6fb6e8 60%, #3d93d6 75%); }
  .brand {
    position: absolute; left: 0; right: 0; top: 78px;
    display: flex; align-items: center; justify-content: center; gap: 10px;
  }
  .brand-dot { width: 46px; height: 46px; border-radius: 50%; background: var(--brand-blue); }
  .brand-name { font-family: "Arimo", sans-serif; font-weight: 700; font-size: 44px; color: #4a4a4a; letter-spacing: -1px; }
  .headline {
    position: absolute; left: 0; right: 0; text-align: center;
    font-family: "Roboto Condensed", sans-serif; font-weight: 700; color: #333;
  }
  .headline--lead { top: 196px; font-size: 27px; }
  .headline--main { top: 232px; font-size: 38px; }
  .front-photo {
    position: absolute; left: 0; top: 305px; width: 386px; height: 320px;
    background: radial-gradient(circle at 58% 28%, #ffffff 0%, #d9ecfa 18%, #7fc0ec 45%, #2f8bd3 100%);
  }
  .front-base {
    position: absolute; left: 0; top: 600px; width: 386px; height: 228px;
    background: linear-gradient(180deg, #2f8fd6 0%, var(--deep-blue) 55%, var(--navy) 100%);
  }
  .services {
    position: absolute; left: 0; right: 0; top: 662px; text-align: center;
    font-family: "Roboto Condensed", sans-serif; font-weight: 700; font-size: 41px; line-height: 46px;
    color: var(--white); text-shadow: 0 2px 3px rgba(0,0,0,.45);
  }
</style>
</head>
<body>
<main class="flyer">

  <section class="panel panel--flap">
    <span class="question-dot" style="top:58px"></span>
    <p class="question" style="top:52px">Are you stuck in a rut or at a crossroads in life?</p>
    <span class="divider" style="top:166px"></span>
    <span class="question-dot" style="top:222px"></span>
    <p class="question" style="top:216px">Do you have ongoing problems with your career, relationship or just life itself?</p>
    <span class="divider" style="top:374px"></span>
    <span class="question-dot" style="top:418px"></span>
    <p class="question" style="top:412px">Would you like to change your direction, or regain some clarity in life?</p>
    <div class="flap-photo" role="img" aria-label="Photo of a signpost against a cloudy sky with arrows reading Balance, Life and Work"></div>
    <svg class="wave" style="top:578px" height="70" viewBox="0 0 386 70" aria-hidden="true">
      <path d="M0 40 C120 10 250 20 386 0 L386 70 L0 70 Z" fill="transparent"/>
      <path d="M0 22 C110 50 240 60 386 4" fill="none" stroke="#cfe3f3" stroke-width="6"/>
      <path d="M0 30 C120 56 250 62 386 14" fill="none" stroke="#1a8fd8" stroke-width="9"/>
      <path d="M0 40 C120 62 260 60 386 30 L386 34 C260 66 120 68 0 46 Z" fill="#0f5f9e"/>
    </svg>
  </section>

  <section class="panel panel--back">
    <h2 class="section-bar" style="top:28px">About us</h2>
    <p class="about-text" style="top:76px">Tall Harbor is a professional coaching service that helps people like you achieve the outcomes that you’re looking for. It doesn’t matter what the challenge is, coaching can take you from where you are now, to where you want to be.</p>
    <p class="about-text" style="top:146px">If you are ready to take your life to the next level and would like to know more, please get in touch. Our introductory sessions are complimentary and totally obligation free, so why not give it a go? We look forward to hearing from you.</p>

    <div class="testimonials">
      <h2>TESTIMONIALS</h2>
      <p class="quote">"There has been laughter, tears, frustration, joy, exhilaration, and "light bulb" moments in every session I have had with Theo. If anyone is even contemplating taking this journey, please for your own sake do....... you will never look back."<span class="quote-name">JENNA R</span></p>
      <p class="quote">“Brindle’s positivity and encouragement really helped me to keep motivated and focused. I found him to be very caring and genuinely interested in helping me realise my strengths and potential”<span class="quote-name">PAULA K</span></p>
    </div>

    <p class="call-to-action">Call now for a <strong>FREE</strong> introductory session or visit our website to download our e-book!</p>

    <h2 class="section-bar" style="top:656px">Contact Us</h2>
    <ul class="contact-list">
      <li class="phone">
        <svg viewBox="0 0 16 16" aria-hidden="true"><path d="M4 1 L6 4 L4.5 6 C5.5 8 8 10.5 10 11.5 L12 10 L15 12 L13.5 15 C7 15 1 9 1 2.5 Z" fill="none" stroke="#333" stroke-width="1.4"/></svg>
        (03) 5550 1827
      </li>
      <li>
        <svg viewBox="0 0 16 16" aria-hidden="true"><rect x="1.5" y="3.5" width="13" height="9" fill="none" stroke="#333" stroke-width="1.4"/><path d="M1.5 3.5 L8 9 L14.5 3.5" fill="none" stroke="#333" stroke-width="1.4"/></svg>
        info@tallharbor-example.com
      </li>
      <li>
        <svg viewBox="0 0 16 16" aria-hidden="true"><circle cx="8" cy="8" r="6.5" fill="none" stroke="#333" stroke-width="1.3"/><ellipse cx="8" cy="8" rx="3" ry="6.5" fill="none" stroke="#333" stroke-width="1.1"/><path d="M1.5 8 H14.5" stroke="#333" stroke-width="1.1"/></svg>
        www.tallharbor-example.com
      </li>
    </ul>
    <p class="abn">ABN. 00 123 456 789</p>
  </section>

  <section class="panel panel--front">
    <div class="brand">
      <span class="brand-dot"></span>
      <span class="brand-name">Tall Harbor</span>
    </div>
    <p class="headline headline--lead">Take control of YOUR LIFE</p>
    <p class="headline headline--main">RIGHT NOW!</p>
    <div class="front-photo" role="img" aria-label="Illustration of a person with outstretched arms silhouetted against a bright sun, with birds in a blue sky"></div>
    <svg class="wave" style="top:572px" height="80" viewBox="0 0 386 80" aria-hidden="true">
      <path d="M0 40 C120 10 260 6 386 30 L386 80 L0 80 Z" fill="#2f8fd6"/>
      <path d="M0 36 C120 6 260 2 386 26" fill="none" stroke="#ffffff" stroke-width="5"/>
      <path d="M0 44 C130 18 270 16 386 40" fill="none" stroke="#7a7a7a" stroke-width="4"/>
      <path d="M0 54 C130 30 270 28 386 52" fill="none" stroke="#bfe0f6" stroke-width="3"/>
    </svg>
    <div class="front-base"></div>
    <p class="services">CAREER,<br>RELATIONSHIP<br>&amp; LIFE COACHING</p>
  </section>

</main>
</body>
</html>
```